High End Notary Service Business Card Design

Want a professional and elegant/luxurious business card that is clean and simple in the design. A notary is a trusted professional that helps people sign very important documents. The card should be in alignment with this service provided.

Most of the time, service will be for the purchase of a home or refinance of a mortgage

There is NO LOGO. This is aesthetic. A look and feel. Conveying professionalism and concierge level of service.

Target Market(s)

Other business professionals, Lawyers, Escrow Officers, Loan Officers

Industry/Entity Type

Legal

Contact Information for Business Card

This will be a one-sided business card

Colors
35a7d7
3176b5
85cae6
d3a5cc
b868aa
ffffff
0356a4

Requirements
Must have
• Lorena T. Mirabel-Hodgkins
Notary Public

642-871-3094
MirabelSigningDesk@Wexmail.com
Nice to have
• Headshot photo below. Convey the aspect of signing documents. No black cards. Preference is shades of blue: light blue, navy, aqua, gold, white, or lavendar, etc.
Should not have
• No scales or legal scales.

```html
<!DOCTYPE html>
<html lang="en">
<head>
<meta charset="utf-8">
<title>Notary Public Business Card – Colour Options</title>
<link href="https://fonts.googleapis.com/css2?family=Poppins:wght@300;400;500&display=swap" rel="stylesheet">
<style>
  :root {
    --backdrop: #ffe6d6;
    --white: #ffffff;
    --aqua: #35a7d7;
    --mid-blue: #3176b5;
    --navy: #0356a4;
    --orchid: #b868aa;
    --lavender: #d3a5cc;
    --photo-cool: #8e93a1;
    --photo-warm: #b39c88;
  }
  * { box-sizing: border-box; margin: 0; padding: 0; }
  html, body {
    width: 1200px; height: 300px; overflow: hidden;
    background: var(--backdrop);
    font-family: "Poppins", sans-serif;
  }
  .sheet { position: relative; width: 1200px; height: 300px; }

  .card {
    position: absolute; top: 17px;
    width: 170px; height: 266px;
    background: var(--white);
    color: var(--white);
    overflow: hidden;
  }
  .card--1 { left: 40.5px; --body: var(--aqua);     --roof: var(--mid-blue); }
  .card--2 { left: 230px;  --body: var(--mid-blue); --roof: var(--navy); }
  .card--3 { left: 419.7px;--body: var(--orchid);   --roof: var(--navy); }
  .card--4 { left: 609.8px;--body: var(--mid-blue); --roof: var(--navy); }
  .card--5 { left: 799.3px;--body: var(--lavender); --roof: var(--aqua); }
  .card--6 { left: 989.4px;--body: var(--navy);     --roof: var(--aqua); }

  .house { position: absolute; inset: 0; width: 170px; height: 266px; }
  .house__roof { fill: var(--roof); }
  .house__body { fill: var(--body); }

  .headshot {
    position: absolute;
    background: linear-gradient(160deg, var(--photo-cool) 0%, var(--photo-cool) 45%, var(--photo-warm) 100%);
    border: 7px solid var(--white);
  }
  .headshot--round {
    left: 33px; top: 47px; width: 104px; height: 104px;
    border-radius: 50%;
  }
  .headshot--framed {
    left: 40px; top: 60.5px; width: 90px; height: 90px;
    box-shadow: 2px 2px 2px rgba(0,0,0,0.25);
  }

  .identity {
    position: absolute; left: 19px; width: 132px; top: 171px;
    text-align: center;
  }
  .card--framed .identity { top: 174px; }
  .identity__name {
    font-size: 10.4px; font-weight: 400; line-height: 14px;
    white-space: nowrap; letter-spacing: 0.05px;
  }
  .identity__rule {
    position: relative; height: 1.3px; margin-top: 3px;
    background: var(--white);
  }
  .identity__rule::after {
    content: ""; position: absolute; left: 50%; top: 50%;
    width: 4px; height: 4px; border-radius: 50%;
    background: var(--white); transform: translate(-50%, -50%);
  }
  .identity__title {
    margin-top: 3.5px;
    font-size: 6.2px; font-weight: 300; letter-spacing: 0.15px;
  }

  .contact {
    position: absolute; left: 19px; top: 221px;
    list-style: none;
    font-size: 6.3px; font-weight: 500; line-height: 8px;
  }
  .contact__item { display: flex; align-items: center; height: 8px; margin-bottom: 4px; }
  .contact__icon { width: 7.5px; height: 6px; margin-right: 5.5px; fill: var(--white); flex: none; }
</style>
</head>
<body>
<main class="sheet">

  <!-- option 1 -->
  <article class="card card--1 card--round">
    <svg class="house" viewBox="0 0 170 266" preserveAspectRatio="none" aria-hidden="true">
      <polygon class="house__roof" points="0,46 85,7.5 170,46 170,55.5 85,16 0,55.5"/>
      <polygon class="house__body" points="0,55.5 85,16 170,55.5 170,266 0,266"/>
    </svg>
    <div class="headshot headshot--round" role="img" aria-label="Headshot portrait of the notary"></div>
    <div class="identity">
      <p class="identity__name">Lorena T. Mirabel-Hodgkins</p>
      <div class="identity__rule"></div>
      <p class="identity__title">NOTARY PUBLIC</p>
    </div>
    <ul class="contact">
      <li class="contact__item"><svg class="contact__icon" viewBox="0 0 10 8"><path d="M0 3 Q5 -1 10 3 L8.5 4 L7 3 L7 2.3 Q5 1.8 3 2.3 L3 3 L1.5 4 Z M2.5 4.2 L7.5 4.2 L9 8 L1 8 Z"/></svg>642-871-3094</li>
      <li class="contact__item"><svg class="contact__icon" viewBox="0 0 10 8"><path d="M0 0 H10 V1 L5 4.5 L0 1 Z M0 2.2 L5 5.7 L10 2.2 V8 H0 Z"/></svg>MirabelSigningDesk@Wexmail.com</li>
    </ul>
  </article>

  <!-- option 2 -->
  <article class="card card--2 card--round">
    <svg class="house" viewBox="0 0 170 266" preserveAspectRatio="none" aria-hidden="true">
      <polygon class="house__roof" points="0,46 85,7.5 170,46 170,55.5 85,16 0,55.5"/>
      <polygon class="house__body" points="0,55.5 85,16 170,55.5 170,266 0,266"/>
    </svg>
    <div class="headshot headshot--round" role="img" aria-label="Headshot portrait of the notary"></div>
    <div class="identity">
      <p class="identity__name">Lorena T. Mirabel-Hodgkins</p>
      <div class="identity__rule"></div>
      <p class="identity__title">NOTARY PUBLIC</p>
    </div>
    <ul class="contact">
      <li class="contact__item"><svg class="contact__icon" viewBox="0 0 10 8"><path d="M0 3 Q5 -1 10 3 L8.5 4 L7 3 L7 2.3 Q5 1.8 3 2.3 L3 3 L1.5 4 Z M2.5 4.2 L7.5 4.2 L9 8 L1 8 Z"/></svg>642-871-3094</li>
      <li class="contact__item"><svg class="contact__icon" viewBox="0 0 10 8"><path d="M0 0 H10 V1 L5 4.5 L0 1 Z M0 2.2 L5 5.7 L10 2.2 V8 H0 Z"/></svg>MirabelSigningDesk@Wexmail.com</li>
    </ul>
  </article>

  <!-- option 3 -->
  <article class="card card--3 card--round">
    <svg class="house" viewBox="0 0 170 266" preserveAspectRatio="none" aria-hidden="true">
      <polygon class="house__roof" points="0,46 85,7.5 170,46 170,55.5 85,16 0,55.5"/>
      <polygon class="house__body" points="0,55.5 85,16 170,55.5 170,266 0,266"/>
    </svg>
    <div class="headshot headshot--round" role="img" aria-label="Headshot portrait of the notary"></div>
    <div class="identity">
      <p class="identity__name">Lorena T. Mirabel-Hodgkins</p>
      <div class="identity__rule"></div>
      <p class="identity__title">NOTARY PUBLIC</p>
    </div>
    <ul class="contact">
      <li class="contact__item"><svg class="contact__icon" viewBox="0 0 10 8"><path d="M0 3 Q5 -1 10 3 L8.5 4 L7 3 L7 2.3 Q5 1.8 3 2.3 L3 3 L1.5 4 Z M2.5 4.2 L7.5 4.2 L9 8 L1 8 Z"/></svg>642-871-3094</li>
      <li class="contact__item"><svg class="contact__icon" viewBox="0 0 10 8"><path d="M0 0 H10 V1 L5 4.5 L0 1 Z M0 2.2 L5 5.7 L10 2.2 V8 H0 Z"/></svg>MirabelSigningDesk@Wexmail.com</li>
    </ul>
  </article>

  <!-- option 4 -->
  <article class="card card--4 card--framed">
    <svg class="house" viewBox="0 0 170 266" preserveAspectRatio="none" aria-hidden="true">
      <polygon class="house__roof" points="0,46 85,7.5 170,46 170,55.5 85,16 0,55.5"/>
      <polygon class="house__body" points="0,55.5 85,16 170,55.5 170,266 0,266"/>
    </svg>
    <div class="headshot headshot--framed" role="img" aria-label="Headshot portrait of the notary"></div>
    <div class="identity">
      <p class="identity__name">Lorena T. Mirabel-Hodgkins</p>
      <div class="identity__rule"></div>
      <p class="identity__title">NOTARY PUBLIC</p>
    </div>
    <ul class="contact">
      <li class="contact__item"><svg class="contact__icon" viewBox="0 0 10 8"><path d="M0 3 Q5 -1 10 3 L8.5 4 L7 3 L7 2.3 Q5 1.8 3 2.3 L3 3 L1.5 4 Z M2.5 4.2 L7.5 4.2 L9 8 L1 8 Z"/></svg>642-871-3094</li>
      <li class="contact__item"><svg class="contact__icon" viewBox="0 0 10 8"><path d="M0 0 H10 V1 L5 4.5 L0 1 Z M0 2.2 L5 5.7 L10 2.2 V8 H0 Z"/></svg>MirabelSigningDesk@Wexmail.com</li>
    </ul>
  </article>

  <!-- option 5 -->
  <article class="card card--5 card--framed">
    <svg class="house" viewBox="0 0 170 266" preserveAspectRatio="none" aria-hidden="true">
      <polygon class="house__roof" points="0,46 85,7.5 170,46 170,55.5 85,16 0,55.5"/>
      <polygon class="house__body" points="0,55.5 85,16 170,55.5 170,266 0,266"/>
    </svg>
    <div class="headshot headshot--framed" role="img" aria-label="Headshot portrait of the notary"></div>
    <div class="identity">
      <p class="identity__name">Lorena T. Mirabel-Hodgkins</p>
      <div class="identity__rule"></div>
      <p class="identity__title">NOTARY PUBLIC</p>
    </div>
    <ul class="contact">
      <li class="contact__item"><svg class="contact__icon" viewBox="0 0 10 8"><path d="M0 3 Q5 -1 10 3 L8.5 4 L7 3 L7 2.3 Q5 1.8 3 2.3 L3 3 L1.5 4 Z M2.5 4.2 L7.5 4.2 L9 8 L1 8 Z"/></svg>642-871-3094</li>
      <li class="contact__item"><svg class="contact__icon" viewBox="0 0 10 8"><path d="M0 0 H10 V1 L5 4.5 L0 1 Z M0 2.2 L5 5.7 L10 2.2 V8 H0 Z"/></svg>MirabelSigningDesk@Wexmail.com</li>
    </ul>
  </article>

  <!-- option 6 -->
  <article class="card card--6 card--framed">
    <svg class="house" viewBox="0 0 170 266" preserveAspectRatio="none" aria-hidden="true">
      <polygon class="house__roof" points="0,46 85,7.5 170,46 170,55.5 85,16 0,55.5"/>
      <polygon class="house__body" points="0,55.5 85,16 170,55.5 170,266 0,266"/>
    </svg>
    <div class="headshot headshot--framed" role="img" aria-label="Headshot portrait of the notary"></div>
    <div class="identity">
      <p class="identity__name">Lorena T. Mirabel-Hodgkins</p>
      <div class="identity__rule"></div>
      <p class="identity__title">NOTARY PUBLIC</p>
    </div>
    <ul class="contact">
      <li class="contact__item"><svg class="contact__icon" viewBox="0 0 10 8"><path d="M0 3 Q5 -1 10 3 L8.5 4 L7 3 L7 2.3 Q5 1.8 3 2.3 L3 3 L1.5 4 Z M2.5 4.2 L7.5 4.2 L9 8 L1 8 Z"/></svg>642-871-3094</li>
      <li class="contact__item"><svg class="contact__icon" viewBox="0 0 10 8"><path d="M0 0 H10 V1 L5 4.5 L0 1 Z M0 2.2 L5 5.7 L10 2.2 V8 H0 Z"/></svg>MirabelSigningDesk@Wexmail.com</li>
    </ul>
  </article>

</main>
</body>
</html>
```